Consulting firm needs elegant, modern designs

Business card design - I have a logo which has previously been developed for Q-Pathways - I will attach. I will also attach specifications for the size of the business card.

We also need a logo design for our leadership consulting product - Form in Guidance - we focus on improving workplace health by educating leaders and learning professionals about how the physical and emotional affects performance and engagement. I have some example logos and ideas which I will attach - these have attempted to bring in the body but I do not like the font (see www.formingguidance-example.com for preferred font). Idea is to please have a 'body' visible somehow in the word Leadership, ensuring that this conveys flexibility and agility. Colors which I prefer are deep purple OR turquoise, together with silver. COLORS below are for LOGO design.

Target Market(s)

For the business card, it should be more masculine. The logo which will be attached should be neutralized into dark blue shades and silver. The business card Q-Pathways is focused on business transformation - organizations who would require a consultant to help them enter new markets, for example.

Industry/Entity Type

Leadership

Contact Information for Business Card

Content:
Q-Pathways
Lindenkade 27
4921KP, Breda, The Netherlands
maurits@Q-Pathways.example
www.Q-Pathways.example

Colors for business card should be conservative and slightly more masculine. Use the Q-Pathways logo but change the colors to blue or shades of gray/black.

Dimensions for cut
85 x 55 mm
1004 x 650 pixels
Full document size
88 x 58 mm
1040 x 685 pixels
For the best result, you need to design the full document size including the bleed

Logo Text

Form in Guidance

Font styles to use
Serif
Sans Serif

Colors
876aae
333333
959595

Requirements
Must have
• Professional, modern and unique business card design
• Professional, elegant, and modern logo design - with creative thinking
Should not have
• Too many colors

```html
<!DOCTYPE html>
<html lang="en">
<head>
<meta charset="utf-8">
<title>Q-Pathways Business Card</title>
<link rel="stylesheet" href="https://fonts.googleapis.com/css2?family=Open+Sans:wght@400;600;700&display=swap">
<style>
  :root {
    --card-bg: #f6f6fb;
    --ink-blue: #3b4ea2;
    --brand-blue: #4a4aa0;
    --mark-blue: #5b5fb0;
  }
  html, body {
    margin: 0;
    padding: 0;
    overflow: hidden;
    background: var(--card-bg);
  }
  .card {
    position: relative;
    width: 1200px;
    height: 790px;
    background: var(--card-bg);
    font-family: "Open Sans", sans-serif;
    color: var(--ink-blue);
    overflow: hidden;
  }
  .accent-bar {
    position: absolute;
    left: 4px;
    width: 5px;
    background: var(--ink-blue);
  }
  .accent-bar--name { top: 53px; height: 88px; }
  .accent-bar--contact { top: 412px; height: 172px; }

  .person {
    position: absolute;
    left: 43px;
    top: 50px;
  }
  .person__name {
    margin: 0;
    font-size: 44px;
    font-weight: 700;
    letter-spacing: 4px;
    line-height: 1;
    text-transform: uppercase;
  }
  .person__role {
    margin: 8px 0 0;
    font-size: 27px;
    font-weight: 400;
    letter-spacing: 3px;
    line-height: 1;
    text-transform: uppercase;
  }

  .contact {
    position: absolute;
    left: 38px;
    top: 408px;
    margin: 0;
    padding: 0;
    list-style: none;
    font-size: 29px;
    line-height: 48px;
  }

  .brand {
    position: absolute;
    right: 12px;
    top: 40px;
    display: flex;
    align-items: center;
    gap: 18px;
  }
  .brand__dot {
    width: 96px;
    height: 96px;
  }
  .brand__name {
    font-size: 54px;
    font-weight: 600;
    color: var(--brand-blue);
    line-height: 1;
  }
</style>
</head>
<body>
  <div class="card">
    <span class="accent-bar accent-bar--name"></span>
    <div class="person">
      <h1 class="person__name">Maurits Dekker</h1>
      <p class="person__role">Manager</p>
    </div>

    <div class="brand">
      <svg class="brand__dot" viewBox="0 0 96 96" aria-hidden="true">
        <circle cx="48" cy="48" r="46" fill="var(--mark-blue)"/>
      </svg>
      <span class="brand__name">Q-Pathways</span>
    </div>

    <span class="accent-bar accent-bar--contact"></span>
    <ul class="contact">
      <li>Lindenkade 27</li>
      <li>4921KP, Breda, The Netherlands</li>
      <li>maurits@Q-Pathways.example</li>
      <li>www.Q-Pathways.example</li>
    </ul>
  </div>
</body>
</html>
```